Cobalt Medispa Business Card

need a business card for our medispa, attached please see the logo.
our website is https://cobaltmedispa-example.com

Sorena Baltik, MD
Internal Medicine

555-204-7183

Sorena@cobaltmedispa-example.com

Www.Cobaltmedispa-example.com

827 E Tollis Blvd N, Ste 540, Katy, TX 77000

Target Market(s)

MedSpa, Cosmetics, Esthetics

Industry/Entity Type

MedicalSpa

Contact Information for Business Card

Please see the attached business card which i pulled from the internet. I like the idea back as a logo and front with info.

Font styles to use
Decorative

Requirements
Must have
• Color should be matching with Logo and Website theme, Also I like to have QR code for the website

```html
<!DOCTYPE html>
<html lang="en">
<head>
<meta charset="utf-8">
<title>Cobalt Medispa Business Card</title>
<link href="https://fonts.googleapis.com/css2?family=Marcellus+SC&family=Lato:wght@400&display=swap" rel="stylesheet">
<style>
  :root {
    --backdrop: #ababab;
    --taupe: #b09683;
    --paper: #ffffff;
    --ink-grey: #6f6f6f;
    --soft-grey: #9a9a9a;
    --mark-grey: #a9a9a9;
    --gold: #c9a13b;
  }
  * { margin: 0; padding: 0; box-sizing: border-box; }
  html, body {
    width: 1200px; height: 1000px; overflow: hidden;
    background: var(--backdrop);
  }
  .stage { position: relative; width: 1200px; height: 1000px; }
  .card {
    position: absolute; left: 294px; width: 613px; height: 352px;
    border-radius: 28px; overflow: hidden;
  }
  .card-front { top: 118px; background: var(--taupe); }
  .card-back { top: 532px; background: var(--paper); }

  .brand-name {
    font-family: "Marcellus SC", serif;
    font-weight: 400;
    white-space: nowrap;
    position: absolute;
  }
  .card-front .brand-name {
    color: var(--paper);
    font-size: 54px;
    left: 0; right: 0; top: 140px;
    text-align: center;
  }
  .card-back .brand-name {
    color: var(--mark-grey);
    font-size: 32px;
    left: 330px; width: 230px; top: 58px;
    text-align: center;
  }

  .identity {
    position: absolute; right: 337px; top: 180px; text-align: right;
  }
  .identity .person {
    font-family: "Marcellus SC", serif;
    font-size: 24px; color: var(--taupe); line-height: 30px;
  }
  .identity .role {
    font-family: "Lato", sans-serif;
    font-size: 17px; color: var(--soft-grey); line-height: 24px;
  }
  .divider {
    position: absolute; left: 298px; top: 178px;
    width: 2px; height: 56px; background: var(--gold);
  }
  .contacts {
    position: absolute; left: 314px; top: 176px; list-style: none;
    font-family: "Lato", sans-serif; font-size: 14.5px; color: var(--ink-grey);
  }
  .contacts li { display: flex; align-items: center; height: 19.5px; }
  .contacts svg { width: 12px; height: 12px; margin-right: 6px; fill: var(--taupe); }

  .address-band {
    position: absolute; left: 0; right: 0; bottom: 0; height: 40px;
    background: var(--taupe);
    display: flex; align-items: center; justify-content: center;
    font-family: "Marcellus SC", serif; font-size: 19px; color: var(--paper);
    letter-spacing: 0.3px;
  }
</style>
</head>
<body>
<main class="stage">
  <section class="card card-front">
    <div class="brand-name">Cobalt Medispa</div>
  </section>

  <section class="card card-back">
    <div class="brand-name">Cobalt Medispa</div>

    <div class="identity">
      <div class="person">Sorena Baltik, MD</div>
      <div class="role">Internal Medicine</div>
    </div>
    <div class="divider"></div>
    <ul class="contacts">
      <li>
        <svg viewBox="0 0 24 24"><path d="M6.6 10.8a15 15 0 0 0 6.6 6.6l2.2-2.2a1 1 0 0 1 1-.25 11.4 11.4 0 0 0 3.6.57 1 1 0 0 1 1 1V20a1 1 0 0 1-1 1A17 17 0 0 1 3 4a1 1 0 0 1 1-1h3.5a1 1 0 0 1 1 1c0 1.25.2 2.45.57 3.6a1 1 0 0 1-.25 1z"/></svg>
        555-204-7183
      </li>
      <li>
        <svg viewBox="0 0 24 24"><path d="M2 5h20v14H2z M3.5 6.5 12 13l8.5-6.5" stroke="#fff" stroke-width="1.5"/></svg>
        sorena@cobaltmedispa-example.com
      </li>
      <li>
        <svg viewBox="0 0 24 24"><circle cx="12" cy="12" r="10"/><path d="M2 12h20M12 2c3 3 3 17 0 20M12 2c-3 3-3 17 0 20M4 7h16M4 17h16" stroke="#fff" stroke-width="1.2" fill="none"/></svg>
        www.cobaltmedispa-example.com
      </li>
    </ul>

    <div class="address-band">827 E Tollis Blvd N, Ste 540, Katy, TX 77000</div>
  </section>
</main>
</body>
</html>
```